Halvern Properties Business Cards

I would like a business card that includes myself and my partner.
Includes: Logo, office #, email, website, our names, our numbers and possibly the address. I would also like the logo to be embossed and the card to be horizontal.
There is a photo of our yard signs to give you an idea of the colors of our business.

Target Market(s)

Everyone in real estate market.
We are in a rural area. Our clientele are from all socioeconomic backgrounds.

Industry/Entity Type

Real Estate Agent

Contact Information for Business Card

Company Name: Halvern Properties
Our Names, Titles & Cell #'s : Marla Halvern-Broker (555).316.4827, Tessa Halvern-Realtor (555).627.9154
Office #: (555).841.2600
Website: halvernproperties-example.com
Joint Email: halvern@halvernproperties-example.com
Office Address: 518B W. Cottonwell Ave.
Cedar Bend, ZZ. 70999

Font styles to use
Serif

Requirements
Must have
• HORIZONTAL, Logo, Myself and my partners names, Our cell #'s, our office #, our website, our email address
Nice to have
• Embossed logo, office address, our titles.

```html
<!DOCTYPE html>
<html lang="en">
<head>
<meta charset="utf-8">
<title>Halvern Properties Business Cards</title>
<link rel="stylesheet" href="https://fonts.googleapis.com/css2?family=EB+Garamond:wght@400;600;700&display=swap">
<style>
  :root {
    --backdrop: #e7e5e4;
    --purple: #4a2163;
    --white: #ffffff;
    --ink-gray: #5a5a5a;
    --band-gray: #666666;
    --shadow: rgba(0, 0, 0, 0.18);
  }
  * { box-sizing: border-box; margin: 0; padding: 0; }
  html, body {
    width: 1200px;
    height: 1189px;
    overflow: hidden;
    background: var(--backdrop);
    font-family: "EB Garamond", Georgia, serif;
  }
  .sheet {
    position: relative;
    width: 1200px;
    height: 1189px;
  }
  .card {
    position: absolute;
    left: 220px;
    width: 760px;
    height: 434px;
    box-shadow: 0 6px 18px var(--shadow);
    overflow: hidden;
  }
  /* Front */
  .card-front {
    top: 120px;
    background: var(--purple);
    color: var(--white);
    text-align: center;
  }
  .card-front .company-name {
    position: absolute;
    top: 150px;
    left: 0;
    right: 0;
    font-size: 62px;
    font-weight: 600;
    letter-spacing: 1px;
  }
  .card-front .website {
    position: absolute;
    top: 290px;
    left: 0;
    right: 0;
    font-size: 19px;
    font-weight: 400;
    letter-spacing: 0.3px;
  }
  /* Back */
  .card-back {
    top: 630px;
    background: var(--white);
  }
  .card-back .company-name {
    position: absolute;
    top: 62px;
    left: 48px;
    font-size: 44px;
    font-weight: 600;
    color: var(--purple);
    letter-spacing: 0.5px;
  }
  .agents {
    position: absolute;
    top: 52px;
    right: 44px;
    width: 250px;
  }
  .agent { margin-bottom: 26px; }
  .agent-name {
    font-size: 27px;
    font-weight: 600;
    color: var(--purple);
    line-height: 1.05;
  }
  .agent-title {
    font-size: 18px;
    color: var(--ink-gray);
    padding-left: 18px;
    line-height: 1.1;
  }
  .agent-phone {
    font-size: 19px;
    color: var(--ink-gray);
    padding-left: 36px;
    line-height: 1.15;
  }
  .label { color: var(--purple); font-weight: 700; }
  .office {
    position: absolute;
    left: 48px;
    top: 238px;
    font-size: 20px;
    font-style: normal;
    line-height: 1.22;
    color: var(--ink-gray);
  }
  .office .indent-1 { padding-left: 16px; }
  .office .indent-2 { padding-left: 36px; }
  .office .indent-3 { padding-left: 54px; }
  .accent-band {
    position: absolute;
    left: 0;
    bottom: 0;
    width: 760px;
    height: 38px;
  }
</style>
</head>
<body>
<main class="sheet">
  <section class="card card-front" aria-label="Card front">
    <div class="company-name">Halvern Properties</div>
    <div class="website">halvernproperties-example.com</div>
  </section>

  <section class="card card-back" aria-label="Card back">
    <div class="company-name">Halvern Properties</div>

    <div class="agents">
      <div class="agent">
        <div class="agent-name">Marla Halvern</div>
        <div class="agent-title">Broker</div>
        <div class="agent-phone"><span class="label">M:</span> (555).316.4827</div>
      </div>
      <div class="agent">
        <div class="agent-name">Tessa Halvern</div>
        <div class="agent-title">Realtor</div>
        <div class="agent-phone"><span class="label">M:</span> (555).627.9154</div>
      </div>
    </div>

    <address class="office">
      <div>518B W. Cottonwell Ave.</div>
      <div class="indent-1">Cedar Bend, ZZ. 70999</div>
      <div class="indent-2"><span class="label">Office:</span> (555).841.2600</div>
      <div class="indent-3"><span class="label">Joint Email:</span> halvern@halvernproperties-example.com</div>
    </address>

    <svg class="accent-band" viewBox="0 0 760 38" aria-hidden="true">
      <polygon points="0,0 600,0 612,19 600,38 0,38" fill="var(--purple)"/>
      <polygon points="614,0 760,0 760,38 614,38 626,19" fill="var(--band-gray)"/>
    </svg>
  </section>
</main>
</body>
</html>
```